brindle's business card for earthmoving and tipper hire business.

I have a small earthmoving and tipper truck company. I am aiming for the smaller jobs that the big guys don't want. I am also Doing grass slashing and fire hazard reduction work. I would like to see some earthy colors, greens browns etc. I have a tractor with a front end loader attachment, and a 22 ton tipper. I would like to maybe have a silhouette of a tipper and tractor/slasher/loader setup in centre with my business name over the top and details to one side or something like that

Industry/Entity Type

Business

Contact Information for Business Card

Brindle's small earthworks and tipper hireToowoombaABN: 47781050480PH 0479126773Email brindle.4@fenwickmail.com

Font styles to use
Sans Serif

Colors
fbee3d
abd036
85cae6
f78f20

Requirements
Nice to have
• Earthy colors . business name in blue

```html
<!DOCTYPE html>
<html lang="en">
<head>
<meta charset="utf-8">
<title>Brindle's Business Card</title>
<link href="https://fonts.googleapis.com/css2?family=Quicksand:wght@500;600;700&display=swap" rel="stylesheet">
<style>
  :root {
    --page-bg: #eef0f2;
    --card-bg: #ffffff;
    --frame-cyan: #85e2ea;
    --brand-orange: #f78f20;
    --tag-brown: #6b3416;
    --text-dark: #1b1b1b;
    --service-green: #5a8a12;
    --service-label: #4a6e0c;
  }
  * { margin: 0; padding: 0; box-sizing: border-box; }
  html, body {
    width: 1200px; height: 848px; overflow: hidden;
    background: var(--page-bg);
    font-family: "Quicksand", sans-serif;
  }
  .stage {
    width: 1200px; height: 848px;
    display: flex; align-items: center; justify-content: center;
  }
  .business-card {
    width: 1000px; height: 606px;
    background: var(--card-bg);
    position: relative;
    box-shadow: 0 4px 18px rgba(0,0,0,0.12);
  }
  .card-frame {
    position: absolute; inset: 26px;
    border: 5px solid var(--frame-cyan);
    border-radius: 26px;
    display: flex; flex-direction: column; align-items: center;
  }
  .brand-row {
    margin-top: 38px;
    display: flex; align-items: center; gap: 30px;
  }
  .vehicle-art {
    width: 180px; height: 96px;
    border-radius: 8px;
    background: linear-gradient(135deg, #3a3a3a, #111);
    opacity: 0.85;
  }
  .brand-lockup { display: flex; flex-direction: column; align-items: center; }
  .brand-name {
    font-size: 86px; font-weight: 700; letter-spacing: 3px;
    color: var(--brand-orange); line-height: 1;
    text-transform: uppercase;
  }
  .brand-tagline {
    margin-top: 10px;
    padding: 6px 12px;
    border: 3px solid var(--tag-brown);
    border-radius: 8px;
    color: var(--tag-brown);
    font-size: 29px; font-weight: 700;
  }
  .contact-block {
    margin-top: 50px;
    text-align: center; color: var(--text-dark);
    font-size: 30px; line-height: 1.25; font-weight: 500;
  }
  .contact-block .business-title { font-weight: 700; }
  .contact-block .town { font-weight: 700; }
  .contact-block .abn { font-size: 15px; font-weight: 500; }
  .services {
    margin-top: auto; margin-bottom: 20px;
    text-align: center;
  }
  .services-label {
    color: var(--service-label); font-weight: 700; font-size: 22px;
  }
  .services-list {
    color: var(--service-green); font-size: 22px; font-weight: 500;
    margin-top: 4px;
  }
</style>
</head>
<body>
<main class="stage">
  <article class="business-card">
    <div class="card-frame">
      <header class="brand-row">
        <div class="vehicle-art" role="img" aria-label="Silhouette of a backhoe loader"></div>
        <div class="brand-lockup">
          <div class="brand-name">Brindle's</div>
          <div class="brand-tagline">Small Earthworks &amp; Tipper Hire</div>
        </div>
        <div class="vehicle-art" role="img" aria-label="Silhouette of a tipper truck"></div>
      </header>

      <section class="contact-block">
        <p class="business-title">Brindle's Small Earthworks &amp; Tipper Hire</p>
        <p><span class="town">Carrowbrook</span> <span class="abn">(ABN: 62194038715)</span></p>
        <p>Contact: 0438571629</p>
        <p>Email: brindle.4@fenwickmail.com</p>
      </section>

      <footer class="services">
        <p class="services-label">Our Services:</p>
        <p class="services-list">Small Earthworks &nbsp;|&nbsp; Slashing &nbsp;|&nbsp; Fire Hazard Reduction &nbsp;|&nbsp; Rural Cleanups &nbsp;|&nbsp; Tipper</p>
      </footer>
    </div>
  </article>
</main>
</body>
</html>
```